Carpet cleaning flyer A5

Members of the Federated Rug Washers Guild
2 Technicians attend every Job
Professionally trained and insured carpet & upholstery cleaners
Sutton Coldfield's Premier carpet cleaning company
Choose from one of these great offers
10% OAP Discount or 10% Discount on production of this leaflet or
Get 3 rooms cleaned for the price of 2 or Get your 3 piece suite cleaned and get your lounge cleaned free of charge or Get more than five rooms cleaned and receive 25% discount
A5 design full colour 2 sides

Tel: 0121 698 3042
www.brindlerugcare.example
Address: Heron Barn, Mill Lane, Oxley, B79 2QT

Target Market(s)

Upmarket residential

Industry/Entity Type

It Company

Requirements
Must have
• Company logo, FRWG Logo, Pictures, address,Telephone number, Website address

```html
<!DOCTYPE html>
<html lang="en">
<head>
<meta charset="utf-8">
<title>Brindle Rug Care – A5 Flyer</title>
<link rel="stylesheet" href="https://fonts.googleapis.com/css2?family=Roboto+Condensed:wght@400;700&display=swap">
<style>
  :root {
    --sea-dark: #1f5f8e;
    --sea-mid: #3f8cc0;
    --sea-light: #8cc3e6;
    --card: #eeeff1;
    --accent: #2b7db5;
    --ink: #1b1b1b;
    --rule: #3a86bb;
    --white: #ffffff;
    --badge-green: #5f8f3a;
    --photo-carpet: #b9b3ab;
    --photo-room: #c9bca4;
  }
  * { box-sizing: border-box; margin: 0; padding: 0; }
  html, body { width: 1200px; height: 851px; overflow: hidden; }
  body {
    font-family: "Roboto Condensed", "Arial Narrow", sans-serif;
    color: var(--ink);
    background: var(--white);
    position: relative;
  }
  .page {
    position: absolute;
    top: 0;
    width: 597px;
    height: 851px;
    background: radial-gradient(ellipse at 50% 55%, var(--sea-light) 0%, var(--sea-mid) 55%, var(--sea-dark) 100%);
  }
  .page--front { left: 0; }
  .page--back { left: 603px; }
  .card {
    position: absolute;
    left: 40px; top: 40px;
    width: 518px; height: 770px;
    background: var(--card);
    border-radius: 30px;
  }
  .page--back .card { left: 37px; }
  .heading {
    position: absolute;
    left: 0; right: 0; top: 27px;
    text-align: center;
    color: var(--accent);
    font-size: 28px;
    font-weight: 400;
    line-height: 34px;
  }
  .rule {
    position: absolute;
    height: 2px;
    background: var(--rule);
  }
  .or {
    position: absolute;
    width: 40px; height: 40px;
    margin-left: -20px;
    border-radius: 50%;
    background: var(--accent);
    color: var(--white);
    font-size: 26px;
    line-height: 36px;
    text-align: center;
  }
  .offer {
    position: absolute;
    left: 42px;
    display: flex;
    align-items: center;
  }
  .offer__value {
    color: var(--accent);
    font-size: 68px;
    letter-spacing: -3px;
    line-height: 1;
    margin-right: 14px;
  }
  .offer__text { font-size: 30px; line-height: 35px; }
  .offer-line {
    position: absolute;
    left: 66px;
    font-size: 31px;
    line-height: 36px;
  }
  .photo {
    position: absolute;
    top: 459px; height: 154px;
  }
  .photo--carpet { left: 35px; width: 227px; background: linear-gradient(160deg, #8d8b88 0%, var(--photo-carpet) 45%, #d8d3cc 100%); }
  .photo--room { left: 270px; width: 207px; background: linear-gradient(135deg, #a99f8a 0%, var(--photo-room) 40%, #2f5d99 70%, #e4dccd 100%); }
  .brand {
    position: absolute;
    display: flex;
    align-items: center;
    gap: 9px;
  }
  .brand__dot {
    width: 20px; height: 20px;
    border-radius: 50%;
    background: var(--accent);
  }
  .brand__name {
    font-size: 24px;
    font-weight: 700;
    color: var(--accent);
    line-height: 1.1;
    white-space: nowrap;
  }
  .contact { position: absolute; }
  .contact__tel { font-size: 27px; line-height: 32px; }
  .contact__web { font-size: 15px; margin-top: 2px; }
  .address {
    position: absolute;
    left: 0; right: 0; top: 747px;
    text-align: center;
    font-size: 16px;
  }
  .features {
    position: absolute;
    left: 67px; top: 360px;
    width: 375px; height: 117px;
    background: var(--accent);
    border-radius: 10px;
    color: var(--white);
    font-size: 23px;
    line-height: 30px;
    padding: 10px 14px 0 18px;
    list-style: none;
  }
  .features li { padding-left: 14px; text-indent: -14px; }
  .features li + li { margin-top: 6px; }
  .features li::before { content: "• "; }
  .membership {
    position: absolute;
    left: 75px; width: 200px; top: 620px;
    text-align: center;
    font-size: 12px;
    line-height: 15px;
  }
  .badge { position: absolute; }
  .badge--guild { left: 84px; top: 654px; width: 180px; height: 81px; background: var(--white); border: 1px solid #d0d0d0; }
  .badge--eco { left: 311px; top: 648px; width: 117px; height: 87px; background: linear-gradient(180deg, #f7f7f2, #dfe6d6); border-radius: 4px; }
  .badge--eco span { position: absolute; left: 28px; top: 22px; width: 60px; height: 44px; border-radius: 8px; background: var(--badge-green); }
</style>
</head>
<body>

<section class="page page--front">
  <div class="card">
    <h2 class="heading">Choose from one of these great offers</h2>
    <div class="rule" style="left:44px;width:428px;top:83px"></div>

    <div class="offer" style="top:96px">
      <span class="offer__value">10%</span>
      <span class="offer__text" style="margin-top:16px">OAP Discount</span>
    </div>
    <div class="rule" style="left:44px;width:428px;top:190px"></div>
    <div class="or" style="left:257px;top:170px">or</div>

    <div class="offer" style="top:220px">
      <span class="offer__value">10%</span>
      <span class="offer__text">Discount on production<br>of this leaflet</span>
    </div>
    <div class="rule" style="left:44px;width:428px;top:318px"></div>
    <div class="or" style="left:257px;top:298px">or</div>

    <div class="offer" style="top:346px">
      <span class="offer__value">25%</span>
      <span class="offer__text">Discount on more than<br>five rooms cleaned</span>
    </div>
    <div class="rule" style="left:44px;width:428px;top:429px"></div>

    <div class="photo photo--carpet" role="img" aria-label="Before and after photo of a carpet being cleaned with an extraction wand"></div>
    <div class="photo photo--room" role="img" aria-label="Technician cleaning a cream sofa cushion in a living room"></div>

    <div class="brand" style="left:40px;top:686px">
      <span class="brand__dot"></span>
      <span class="brand__name">Brindle Rug Care</span>
    </div>
    <div class="contact" style="left:258px;top:684px">
      <div class="contact__tel">Tel: 0121 698 3042</div>
      <div class="contact__web">www.brindlerugcare.example</div>
    </div>

    <p class="address">Heron Barn, Mill Lane, Oxley, B79 2QT</p>
  </div>
</section>

<section class="page page--back">
  <div class="card">
    <h2 class="heading">Choose from one of these great offers</h2>
    <div class="rule" style="left:45px;width:430px;top:83px"></div>

    <p class="offer-line" style="top:102px">Get your 3 piece suite cleaned<br>and get your lounge cleaned<br>free of charge</p>
    <div class="rule" style="left:45px;width:430px;top:230px"></div>
    <div class="or" style="left:259px;top:210px">or</div>

    <p class="offer-line" style="top:260px">Get 3 rooms cleaned for the<br>price of 2</p>
    <div class="rule" style="left:45px;width:425px;top:348px"></div>

    <ul class="features">
      <li>2 Technicians attend every job</li>
      <li>Professionally trained and insured carpet &amp; upholstery cleaners</li>
    </ul>

    <div class="brand" style="left:46px;top:548px">
      <span class="brand__dot"></span>
      <span class="brand__name">Brindle Rug Care</span>
    </div>
    <div class="contact" style="left:270px;top:546px">
      <div class="contact__tel">Tel: 0121 698 3042</div>
      <div class="contact__web">www.brindlerugcare.example</div>
    </div>

    <p class="membership">Members of the Federated Rug Washers Guild</p>
    <div class="badge badge--guild" role="img" aria-label="Federated Rug Washers Guild membership badge"></div>
    <div class="badge badge--eco" role="img" aria-label="Eco-friendly cleaning badge"><span></span></div>

    <p class="address">Heron Barn, Mill Lane, Oxley, B79 2QT</p>
  </div>
</section>

</body>
</html>
```